Brochure Design Project

We are looking for a brochure to communicate the various different program we offer within the "Trail & Habitat Studies" department
( www.fieldtrek.rv82.qz.ca )
We have a large photo bank of students engaged in our programs and can willingly provide them if requested.

Target Market(s)

parents, students, academics, administrators

Industry/Entity Type

Bank

Requirements
Must have
• nature based theme. adventure and ecology.

```html
<!DOCTYPE html>
<html lang="en">
<head>
<meta charset="utf-8">
<title>Trail &amp; Habitat Studies Brochure</title>
<link rel="stylesheet" href="https://fonts.googleapis.com/css2?family=Anton&family=Archivo+Black&family=Arimo:ital,wght@0,400;0,700;1,400&display=swap">
<style>
:root{
  --teal:#0f4a52;
  --green:#8cc63f;
  --orange:#f15a24;
  --rust:#a3381f;
  --yellow:#f5d24a;
  --white:#ffffff;
  --bg:#ececec;
}
*{box-sizing:border-box;margin:0;padding:0}
html,body{width:1200px;height:900px;overflow:hidden}
body{background:radial-gradient(ellipse at center,#fff 30%,var(--bg) 100%);font-family:"Arimo",Arial,sans-serif;position:relative}
.spread{position:absolute;left:305px;width:655px;overflow:hidden;display:flex}
.spread--outside{top:71px;height:327px}
.spread--inside{top:500px;height:310px}
.panel{position:relative;height:100%;overflow:hidden}
.panel--teal{background:var(--teal)}
.panel--rust{background:var(--rust)}
.panel--yellow{background:var(--yellow)}
.section-title{position:absolute;font-family:"Archivo Black",sans-serif;font-size:12px;line-height:12px;z-index:5;
  text-shadow:-1px -1px 0 #fff,1px -1px 0 #fff,-1px 1px 0 #fff,1px 1px 0 #fff}
.section-title--green{color:var(--green)}
.section-title--orange{color:var(--orange)}
.card{position:absolute;border:3px solid var(--white);border-radius:12px;color:var(--white);font-size:6.2px;line-height:7.3px;padding:8px 9px;z-index:2}
.card--green{background:var(--green)}
.card--orange{background:var(--orange)}
.card p{margin-bottom:5px}
.card .quote{font-style:italic;opacity:.95}
.card .bold{font-weight:700}
.card--small{font-size:5.8px;line-height:6.8px}
.photo{position:absolute;border:3px solid var(--white);border-radius:50%;z-index:1}
.photo--front{z-index:4}
.dot{position:absolute;border-radius:50%;z-index:2}
.quote-circle{position:absolute;border-radius:50%;background:var(--green);border:3px solid var(--white);color:var(--white);
  font-size:5.8px;line-height:7px;font-style:italic;text-align:center;padding:28px 26px;z-index:2}
.headline{position:absolute;left:15px;top:198px;font-family:"Anton",sans-serif;font-size:21.5px;line-height:22px;letter-spacing:.3px;z-index:2}
.headline .hl-orange{color:var(--orange);display:block}
.headline .hl-white{color:var(--white);display:block}
.brand-badge{position:absolute;left:155px;top:260px;width:55px;height:55px;border-radius:50%;background:var(--white);
  display:flex;align-items:center;justify-content:center;font-family:"Arimo",sans-serif;font-weight:700;font-size:9px;color:var(--teal);z-index:2}
.hero-photo{position:absolute;left:0;top:0;width:220px;height:180px;
  background:linear-gradient(160deg,#f6c25a 0%,#d97a1e 40%,#5b4a1c 75%,#2d3a1a 100%)}
.hero-curve{position:absolute;left:0;top:140px;z-index:2}
.url{font-family:"Archivo Black",sans-serif;font-size:11.5px;color:var(--white)}
</style>
</head>
<body>

<section class="spread spread--outside">
  <div class="panel panel--teal" style="width:218px">
    <h2 class="section-title section-title--green" style="left:22px;top:8px">Trail &amp; Habitat Studies<br>Department</h2>
    <div class="card card--green" style="left:15px;top:24px;width:197px;height:122px;padding-top:10px">
      <p>The Trail &amp; Habitat Studies Department is dedicated to providing students with educational opportunities that reinforce their connection to the natural world and foster sustainability. We focus on giving students the necessary skills to think critically about personal choices and the relationships between society, economy, culture and the environment. Through action leadership, skill development and inspired experience, our students are empowered to make positive change in their communities. We offer numerous programs and have highlighted a few in this document.</p>
    </div>
    <div class="photo photo--front" role="img" aria-label="Photo of a hand with a pen tracing a route on a map" style="left:10px;top:131px;width:96px;height:96px;background:radial-gradient(circle at 40% 40%,#e8e0cf,#b9a58a 60%,#7b6a55)"></div>
    <span class="dot" style="left:151px;top:174px;width:11px;height:11px;background:var(--white)"></span>
    <span class="dot" style="left:168px;top:155px;width:24px;height:24px;background:var(--green)"></span>
    <div class="quote-circle" style="left:38px;top:199px;width:178px;height:178px">"The Trail &amp; Habitat Studies Programs in Riverbend District 82 help to fill a huge void in modern society: the real link between what's taught in the classroom and the day-to-day miracles happening outside. I can think of no better way to close that gap than to get kids into wild areas where Nature does the teaching, affecting students in ways that stick with them for the rest of their lives."<br>Mara Lindqvist,<br>Explorer, Wildlife Biologist, Author</div>
  </div>

  <div class="panel panel--rust" style="width:217px">
    <h2 class="section-title section-title--orange" style="left:15px;top:9px">Go outdoors!</h2>
    <div class="card card--orange" style="left:10px;top:21px;width:200px;height:286px;padding-top:10px">
      <p>Why is it important to spend time outdoors?<br>Well, here is what the research says!</p>
      <p>Regular contact with nature promotes healthier social behavior and lessens social dysfunction, helps alleviate stress, improves resilience, promotes optimal psychological functioning, improves recovery from physical trauma, and reduces mortality.</p>
      <p>A child's time in nature provides the benefits of creating sacred places, development of self and greater independence.</p>
      <p>Children with ADHD who regularly play in green settings have milder symptoms than children who play in built outdoor and indoor settings.</p>
      <p>School gardens positively impact children's learning and behavior.</p>
      <p>Pregnant women living in areas with more trees had better birth outcomes.</p>
      <p>Outdoor experience for teens has self-reported life-changing results.</p>
      <p>Children's emotional affinity towards nature is a strong predictor of their willingness to protect the environment.</p>
      <p>All research summarized &amp; provided by the Kids Outside Network<br>www.kidsoutside.qz.org</p>
    </div>
    <div class="photo photo--front" role="img" aria-label="Close-up photo of hiking boots on a trail" style="left:128px;top:258px;width:90px;height:90px;background:radial-gradient(circle at 50% 45%,#d9b48a,#8a6a4a 60%,#3b3227)"></div>
  </div>

  <div class="panel panel--teal" style="width:220px">
    <div class="hero-photo" role="img" aria-label="Photo of students standing in a sunlit field at sunset"></div>
    <svg class="hero-curve" width="220" height="50" viewBox="0 0 220 50">
      <path d="M0 38 Q110 60 220 0 L220 50 L0 50 Z" fill="var(--teal)"/>
      <path d="M0 38 Q110 60 220 0" fill="none" stroke="#fff" stroke-width="3"/>
    </svg>
    <h1 class="headline">
      <span class="hl-orange">LEADERSHIP</span>
      <span class="hl-white">CITIZENSHIP&amp;</span>
      <span class="hl-orange">OUTDOOR</span>
      <span class="hl-orange">ADVENTURE</span>
    </h1>
    <div class="brand-badge">WRLP</div>
  </div>
</section>

<section class="spread spread--inside">
  <div class="panel panel--teal" style="width:220px">
    <h2 class="section-title section-title--green" style="left:14px;top:8px">Wild Ridge Leadership<br>Program</h2>
    <div class="card card--green card--small" style="left:-3px;top:19px;width:213px;height:140px;padding:16px 10px 6px 12px">
      <p class="quote">"I have never experienced a sensation like this before and at first, I could not put my finger on what it was, but then I realized it was bliss."<br>– Lena (WRLP Alumni)</p>
      <p class="quote">"In finding the gifts and potential of others, we discover and unleash a deeper appreciation for ourselves."<br>– Priya (WRLP Alumni)</p>
      <p class="quote">WRLP offers secondary students an applied field-course in Leadership Studies. During this 9-day summer outdoor immersion, students will develop their Action-Centered leadership skills. The climax of WRLP is the Journey, which is taken through a modality of choice (Aboard, Voyageur, SUP). WRLP is a transformative passage where learners develop a deeper relational understanding of themselves within the greater cultural and biological ecology of the Pacific Northwest.</p>
    </div>
    <div class="photo" role="img" aria-label="Photo of a group of students with backpacks hiking along a forest road" style="left:-40px;top:148px;width:250px;height:250px;background:linear-gradient(170deg,#b8c9a0 0%,#5f7d43 45%,#3b4a2f 80%,#8d8a80 100%)"></div>
  </div>

  <div class="panel panel--rust" style="width:215px">
    <div class="photo" role="img" aria-label="Photo of students doing yoga on paddleboards on the water" style="left:-45px;top:-25px;width:265px;height:175px;background:linear-gradient(180deg,#c9d3d6 0%,#7f98a3 45%,#3f5b66 100%);z-index:3"></div>
    <span class="dot" style="left:180px;top:147px;width:10px;height:10px;background:var(--white)"></span>
    <span class="dot" style="left:195px;top:138px;width:18px;height:18px;background:var(--orange)"></span>
    <h2 class="section-title section-title--orange" style="left:12px;top:154px">Granite Ridge Academy</h2>
    <div class="card card--orange" style="left:7px;top:164px;width:202px;height:132px;padding-top:10px">
      <p class="quote">"Not only was the Granite Ridge Academy program the most engaging educational experience, it also inspired me to look at my community and our environment in a profoundly new light."<br>– Elias (GRA Alumni)</p>
      <p>The Granite Ridge Academy (GRA) is an enriched outdoor education program which focuses on character development through Leadership, Citizenship and Outdoor Adventure. This semester-long program offers students a unique opportunity to obtain high school credits, hard-skills, and outdoor certifications that prepare students for future careers and studies. The program often includes an international service project and a practicum delivering a overnight environmental education program for all grade seven students in the district.</p>
    </div>
  </div>

  <div class="panel panel--yellow" style="width:220px">
    <h2 class="section-title section-title--orange" style="left:16px;top:8px">Sustainability Toolbox</h2>
    <div class="card card--orange card--small" style="left:10px;top:19px;width:215px;height:158px;border-right:none;border-radius:12px 0 0 12px;padding:12px 30px 8px 9px">
      <p class="quote">"Inspiration... it comes to me when I realize that big problems have simple solutions that are within reach and already exist."<br>– Owen (RST Alumni)</p>
      <p class="bold">The Riverbend Sustainability Toolbox is a unique and experience-based youth leadership program that brings together students who are passionate about influencing sustainability in their schools and school communities through action, collaboration, and leadership. This action-packed credit course includes an 8 day field camp in August and a number of weekend sessions throughout the fall. The course features a wide range of fun and experiential learning and leadership development opportunities designed to develop the knowledge and skills necessary to take action for sustainability.</p>
    </div>
    <div class="photo photo--front" role="img" aria-label="Photo of hands holding soil" style="left:178px;top:130px;width:44px;height:44px;background:radial-gradient(circle,#c89a72,#7a5a3e)"></div>
    <div class="photo photo--front" role="img" aria-label="Photo of students silhouetted against a sunset" style="left:5px;top:160px;width:108px;height:108px;background:linear-gradient(180deg,#f2c07a 0%,#d2875a 45%,#2e2622 80%)"></div>
    <div class="photo photo--front" role="img" aria-label="Photo of students gathered outdoors among trees" style="left:120px;top:155px;width:66px;height:66px;background:radial-gradient(circle,#a9c48d,#4f6b3b)"></div>
    <h2 class="section-title section-title--orange" style="left:18px;top:240px">More Information</h2>
    <div class="card card--orange" style="left:10px;top:252px;width:215px;height:40px;border-right:none;border-radius:8px 0 0 8px;display:flex;align-items:center">
      <span class="url">www.fieldtrek.rv82.qz.ca</span>
    </div>
  </div>
</section>

</body>
</html>
```